Bold and modern Raw Manuka Honey label needed

We are needing a new label for one of our honey brands.
Raw Manuka honey has a lot of health benefits and we need a label to look appealing to health minded people but still looking like a jar of honey.
Manuka honey is a very high valued product that we export all over the world so we are looking for a clean and easy to read label as a lot of our customers are foreign and struggle with reading complex labels.
Be creative.... we have a logo and i will add it soon.
I was thinking of adding a silhouette of a bear to go with the Pell Honey name but I'm very open to anything..
Target Market(s)
Health and medical retail shops.
Industry/Entity Type
Health And Wellness
Requirements
Must have
- Brand name is "ambrel"
- Attached is our other label that we are looking at changing as well.
- Company details...
- Pell Honey NZ Limited
- 4/18 Brindle Street
- Central Auckland
- PO Box 41-582
- Auckland
- pellhoneynz@maildrop-nz.com
- www.pellhoneynz-shop.com
Nice to have
- Easy to read.
Should not have
- Hard to read fonts

```html
<!DOCTYPE html>
<html lang="en">
<head>
<meta charset="utf-8">
<title>Ambrel Manuka Honey – Label Set</title>
<link href="https://fonts.googleapis.com/css2?family=Arvo:wght@400;700&family=Roboto+Slab:wght@400;600;800&display=swap" rel="stylesheet">
<style>
  :root {
    --backdrop: #e8eaeb;
    --paper: #ffffff;
    --ink: #141414;
    --ink-soft: #3a3a3a;
    --honey-yellow: #ffe100;
    --pale-yellow: #fff6c4;
    --rule: #e3d24a;
    --grey-mark: #8a8a8a;
  }
  * { box-sizing: border-box; margin: 0; padding: 0; }
  html, body { width: 1200px; height: 800px; overflow: hidden; }
  body {
    background: var(--backdrop);
    font-family: "Roboto Slab", Georgia, serif;
    color: var(--ink);
  }
  .label-set {
    width: 1200px; height: 800px;
    display: flex; align-items: center; justify-content: center; gap: 30px;
  }
  .label {
    position: relative;
    width: 360px; height: 370px;
    background: var(--paper);
    overflow: hidden;
    box-shadow: 0 2px 10px rgba(0,0,0,0.06);
  }
  .silhouette {
    position: absolute;
    background: var(--pale-yellow);
    border-radius: 40% 55% 30% 45% / 45% 40% 55% 35%;
  }
  .label--back .silhouette { left: 40px; top: 90px; width: 270px; height: 250px; }
  .label--story .silhouette { left: 10px; top: 60px; width: 300px; height: 200px; }

  /* Nutrition panel */
  .nutrition {
    position: absolute; left: 78px; top: 30px; width: 234px;
    font-size: 8.5px;
  }
  .nutrition__head {
    display: grid; grid-template-columns: 1fr 48px 48px;
    background: var(--honey-yellow);
  }
  .nutrition__title {
    font-family: "Arvo", serif; font-weight: 700; font-size: 12.5px; line-height: 1.05;
    padding: 8px 4px 2px;
  }
  .nutrition__serving { padding: 0 4px 6px; font-size: 8px; line-height: 1.25; }
  .nutrition__col {
    text-align: center; font-size: 8px; line-height: 1.2; padding-top: 22px;
    border-left: 1px solid var(--paper);
  }
  .nutrition__row {
    display: grid; grid-template-columns: 1fr 48px 48px;
    border-bottom: 1px solid var(--rule);
    padding: 3px 4px; line-height: 1.35;
  }
  .nutrition__row span + span { text-align: center; }
  .nutrition__ingredients {
    display: flex; gap: 6px; background: var(--honey-yellow);
    padding: 5px 4px; font-size: 7.5px; line-height: 1.3; margin-top: 3px;
  }
  .company {
    position: absolute; left: 78px; top: 250px; font-size: 8.5px; line-height: 1.45;
  }
  .company__name { font-size: 13px; color: var(--ink-soft); margin-bottom: 3px; }
  .company__web { font-family: "Arvo", serif; font-weight: 700; font-size: 12px; margin-top: 3px; }

  /* Front */
  .label--front { text-align: center; }
  .comb-pattern {
    position: absolute; left: 130px; top: 100px; width: 100px; height: 215px;
    background: linear-gradient(180deg, var(--pale-yellow), #fffbe0);
    border-radius: 30px 30px 50px 50px;
  }
  .maker {
    position: absolute; top: 48px; left: 0; right: 0;
    display: flex; justify-content: center; align-items: center; gap: 6px;
    font-weight: 800; font-size: 13px;
  }
  .maker__mark { width: 12px; height: 12px; background: var(--ink); }
  .brand {
    position: absolute; top: 100px; left: 0; right: 0;
    font-family: "Arvo", serif; font-weight: 700; font-size: 70px; letter-spacing: -1px; line-height: 1;
  }
  .certified { position: absolute; top: 198px; left: 0; right: 0; font-size: 14px; letter-spacing: 0.5px; }
  .variety {
    position: absolute; top: 222px; left: 0; right: 0;
    font-family: "Arvo", serif; font-weight: 700; font-size: 20px; letter-spacing: 1.5px;
  }
  .origin {
    position: absolute; left: 82px; top: 300px; width: 50px; text-align: center;
    font-size: 5.5px; color: var(--ink-soft);
  }
  .origin__emblem { display: block; width: 44px; height: 22px; margin: 0 auto 2px; background: var(--grey-mark); border-radius: 2px; }
  .weight { position: absolute; right: 60px; top: 304px; font-weight: 600; font-size: 15px; color: var(--ink-soft); }

  /* Story */
  .story {
    position: absolute; left: 42px; top: 48px; width: 280px;
    font-size: 12.5px; line-height: 1.65;
  }
  .story__rule { position: absolute; left: 32px; right: 30px; top: 188px; border-top: 2px dotted var(--honey-yellow); }
  .mgo {
    position: absolute; left: 42px; top: 205px; width: 232px; font-size: 8.5px;
  }
  .mgo__title { text-align: center; font-weight: 600; font-size: 12px; margin-bottom: 8px; }
  .mgo__grid { display: grid; grid-template-columns: 1fr 1fr 1fr; }
  .mgo__head { background: var(--honey-yellow); font-weight: 600; text-align: center; padding: 2px 0; font-size: 8px; }
  .mgo__cell { padding: 4px 0 4px 18px; border-bottom: 1px solid var(--rule); }
  .mgo__grade { grid-column: 3; grid-row: 2 / span 5; display: flex; flex-direction: column; align-items: center; justify-content: space-between; padding: 4px 0; border-bottom: 1px solid var(--rule); }
  .mgo__grade svg { display: block; }
</style>
</head>
<body>
<main class="label-set">

  <section class="label label--back">
    <div class="silhouette" role="img" aria-label="Faint bear silhouette in pale yellow"></div>
    <div class="nutrition">
      <div class="nutrition__head">
        <div>
          <p class="nutrition__title">NUTRITIONAL<br>INFORMATION</p>
          <p class="nutrition__serving">Servings per package: 50<br>Serving size: 10g</p>
        </div>
        <p class="nutrition__col">Qty<br>per<br>Serve</p>
        <p class="nutrition__col">Qty<br>per<br>100g</p>
      </div>
      <div class="nutrition__row"><span>Energy</span><span>132kJ</span><span>1320kJ</span></div>
      <div class="nutrition__row"><span>Protein</span><span>&lt;0.1g</span><span>0.4g</span></div>
      <div class="nutrition__row"><span>Total Fat<br>&nbsp;- Saturated</span><span>0g<br>0g</span><span>0g<br>0g</span></div>
      <div class="nutrition__row"><span>Carbohydrates<br>&nbsp;- Sugars</span><span>8.0g<br>7.8g</span><span>80g<br>78g</span></div>
      <div class="nutrition__row"><span>Sodium</span><span>1.2mg</span><span>12mg</span></div>
      <div class="nutrition__ingredients"><span>INGREDIENTS:</span><span>100% Pure New Zealand Honey, Pollen, Certified MGO 800+</span></div>
    </div>
    <address class="company" style="font-style:normal">
      <p class="company__name">Pell Honey NZ Limited</p>
      <p>4/18 Brindle Street, Auckland Central</p>
      <p>PO Box 41-582, New Zealand</p>
      <p>pellhoneynz@maildrop-nz.com</p>
      <p class="company__web">www.pellhoneynz-shop.com</p>
    </address>
  </section>

  <section class="label label--front">
    <div class="comb-pattern" role="img" aria-label="Faint yellow honeycomb and drop pattern"></div>
    <p class="maker"><span class="maker__mark"></span>Pell Honey</p>
    <h1 class="brand">Ambrel</h1>
    <p class="certified">CERTIFIED MGO 800+</p>
    <p class="variety">MANUKA HONEY</p>
    <p class="origin"><span class="origin__emblem" role="img" aria-label="New Zealand origin emblem"></span>NEW ZEALAND</p>
    <p class="weight">500g</p>
  </section>

  <section class="label label--story">
    <div class="silhouette" role="img" aria-label="Faint bear silhouette in pale yellow"></div>
    <p class="story">Ambrel brings you 35 years of quality honey. Our honeys are 100% pure natural and nothing added. Honey the way it should bee. Best stored at room temperature and away from direct sunlight.</p>
    <div class="story__rule"></div>
    <div class="mgo">
      <p class="mgo__title">DIETARY MGO CONTENT</p>
      <div class="mgo__grid">
        <div class="mgo__head">MGO</div><div class="mgo__head">NPA</div><div class="mgo__head">GRADE</div>
        <div class="mgo__cell">MGO30+</div><div class="mgo__cell">2+</div>
        <div class="mgo__grade">
          <span>General</span>
          <svg width="10" height="34" viewBox="0 0 10 34"><line x1="5" y1="0" x2="5" y2="31" stroke="#ffe100" stroke-width="1.5"/><path d="M1 26 L5 32 L9 26" fill="none" stroke="#ffe100" stroke-width="1.5"/></svg>
          <span>Premium</span>
        </div>
        <div class="mgo__cell">MGO100+</div><div class="mgo__cell">5+</div>
        <div class="mgo__cell">MGO250+</div><div class="mgo__cell">10+</div>
        <div class="mgo__cell">MGO500+</div><div class="mgo__cell">15+</div>
        <div class="mgo__cell">MGO800+</div><div class="mgo__cell">20+</div>
      </div>
    </div>
  </section>

</main>
</body>
</html>
```